Financial Advisor / Asset Manager Zup Design

I'm currently hosting with Zup and my first attempt at a website is live at www.ravenholtwealth.example Clearly I am not a web designer and I need help making this more catchy, modern, cross-platform compatible, search engine optimized, etc. I've got logos, hex color pallets, and a slew of other graphics. I'm interested in working with a winning designer to write/refine my copy/language to complete the build.

Full set of graphics https://pics.lumora-share.example/q71TzR05KwPd2MhXN do NOT use the CONSULTING graphics as this is for a related business / different website

Target Market(s)

Individuals, small institutions, endowments, non-profits seeking financial advice and asset / portfolio management

Industry/Entity Type

Financial Services

Coding

Coded - Design and coding required

Font styles to use
Other font styles liked:
• AvenirLTStd - Black, Book, and Roman as appropriate

Requirements
Must have
• Complete, cross platform website integrating my existing logo
Nice to have
• Easy to update format for go-forward maintenance

```html
<!DOCTYPE html>
<html lang="en">
<head>
<meta charset="utf-8">
<title>Ravenholt Wealth — Financial Planning &amp; Asset Management</title>
<link rel="stylesheet" href="https://fonts.googleapis.com/css2?family=Montserrat:wght@400;500;600;700;800&family=Mulish:wght@400;600;700&display=swap">
<style>
:root{
  --blue:#1a77c9;
  --blue-deep:#0f5fa8;
  --blue-line:#9cc8ec;
  --ink:#1e2226;
  --muted:#555c63;
  --mist:#eef1f4;
  --white:#ffffff;
  --black:#000000;
}
*{box-sizing:border-box;margin:0;padding:0}
html,body{width:1200px;height:5034px;overflow:hidden}
body{position:relative;background:var(--white);font-family:"Mulish",sans-serif;color:var(--ink)}
.abs{position:absolute}
.head-font{font-family:"Montserrat",sans-serif}

/* hero */
.hero{left:0;top:0;width:1200px;height:790px}
.nav{left:0;top:72px;width:1200px;height:40px}
.nav a{position:absolute;color:var(--white);text-decoration:none;font-family:"Montserrat",sans-serif;font-size:14px;font-weight:500;letter-spacing:.5px;top:10px;white-space:nowrap}
.nav a.active::after{content:"";position:absolute;left:0;right:0;bottom:-8px;height:2px;background:var(--white)}
.nav .contact-btn{border:2px solid var(--white);padding:11px 22px;top:0}
.brand{left:500px;top:76px;width:205px;text-align:center;color:var(--white);font-family:"Montserrat",sans-serif;font-size:22px;font-weight:500;letter-spacing:1px;line-height:1.1}
.hero-claim{color:var(--white);font-family:"Montserrat",sans-serif;font-weight:800;font-size:27px;line-height:35px;text-align:center;text-transform:uppercase;white-space:nowrap;text-shadow:0 2px 6px rgba(0,0,0,.35)}

/* section titles */
.eyebrow{width:1200px;left:0;text-align:center;font-family:"Montserrat",sans-serif;font-size:15px;letter-spacing:2px;color:var(--muted)}
.title{width:1200px;left:0;text-align:center;font-family:"Montserrat",sans-serif;font-size:35px;font-weight:700;color:var(--blue)}

/* services */
.service h3{font-family:"Montserrat",sans-serif;font-weight:600;font-size:27px;color:var(--ink);margin-bottom:22px}
.service p{font-size:14.5px;line-height:24px;color:var(--muted);width:450px}
.btn-outline{display:inline-block;margin-top:30px;border:2px solid var(--blue);color:var(--blue);font-family:"Montserrat",sans-serif;font-weight:700;font-size:13px;padding:13px 32px;text-decoration:none;letter-spacing:.5px;white-space:nowrap}
.art{background:linear-gradient(135deg,#e3f0fb,#c9e1f6);border-radius:14px}

/* about */
.about-copy{left:250px;top:2830px;width:700px;text-align:center;font-size:20px;line-height:33px;color:var(--muted)}

/* why */
.feature{font-family:"Montserrat",sans-serif}
.feature h4{font-size:15px;font-weight:700;color:var(--ink);margin-bottom:6px}
.feature p{font-family:"Mulish",sans-serif;font-size:12.5px;line-height:20px;color:var(--muted)}
.badge{width:90px;height:90px;border-radius:50%;background:var(--blue)}

/* contact */
.contact h2{font-family:"Montserrat",sans-serif;font-size:33px;font-weight:700;color:var(--white)}
.contact p,.contact span{color:var(--white);font-size:16px}
.field{position:absolute;width:218px;border-bottom:1px solid #bfc4c9}
.field label{display:block;font-size:12px;color:#8d949a;margin-bottom:6px}
.field div{font-size:16px;color:var(--ink);padding-bottom:10px}

/* footer */
.footer{color:var(--white)}
.footer h5{font-family:"Montserrat",sans-serif;font-size:14px;font-weight:700;letter-spacing:.5px}
.footer li{list-style:none;font-size:14px;line-height:27px}
.footer .rule{position:absolute;width:2px;background:var(--white)}
</style>
</head>
<body>

<!-- HERO -->
<div class="abs hero" role="img" aria-label="Mountain range reflected in a calm alpine lake with forested shore, under a blue sky"
  style="background:linear-gradient(180deg,#3f8fd8 0%,#7fb3df 22%,#c8d8e4 34%,#6b7f6a 48%,#3f5b3a 58%,#5c7fa2 72%,#2c5d88 100%);clip-path:ellipse(95% 100% at 50% 0%)"></div>
<svg class="abs" style="left:0;top:560px" width="1200" height="240" viewBox="0 0 1200 240">
  <path d="M100 150 Q600 290 1100 150" fill="none" stroke="var(--blue)" stroke-width="7"/>
  <path d="M588 168 l12 10 l12 -10" fill="none" stroke="#fff" stroke-width="3"/>
</svg>

<nav class="abs nav">
  <a class="active" style="left:150px">HOME</a>
  <a style="left:263px">ABOUT US</a>
  <a style="left:400px">SERVICES</a>
  <a style="left:740px">FAQS</a>
  <a class="contact-btn" style="left:830px">CONTACT US</a>
  <a style="left:995px">&#9742; (555) 214-0937</a>
</nav>
<div class="abs brand">RAVENHOLT<br><span style="font-size:13px;letter-spacing:3px">WEALTH</span></div>

<svg class="abs" style="left:340px;top:390px" width="520" height="140" viewBox="0 0 520 140">
  <g fill="none" stroke="#fff" stroke-width="3">
    <path d="M255 20 V60 Q255 80 235 80 H30 Q23 80 23 95 V125"/>
    <path d="M275 20 V60 Q275 80 295 80 H490 Q497 80 497 95 V125"/>
  </g>
  <circle cx="23" cy="127" r="5" fill="#fff"/><circle cx="497" cy="127" r="5" fill="#fff"/>
</svg>
<div class="abs hero-claim" style="left:140px;top:530px;width:470px">Personalized financial<br>advice to help you<br>achieve your goals</div>
<div class="abs hero-claim" style="left:596px;top:530px;width:480px">Professional management<br>to make your money<br>work for you</div>

<!-- SERVICES -->
<div class="abs eyebrow" style="top:866px">WHAT WE DO</div>
<div class="abs title" style="top:884px">OUR SERVICES</div>

<svg class="abs" style="left:0;top:1300px" width="1200" height="940" viewBox="0 0 1200 940">
  <g fill="none" stroke="var(--blue-line)" stroke-width="3">
    <path d="M527 10 V95 Q527 118 550 118 H695 Q718 118 718 141 V170"/>
    <path d="M683 395 V470 Q683 493 660 493 H515 Q492 493 492 516 V545"/>
    <path d="M507 780 V860 Q507 883 530 883 H675 Q698 883 698 906 V935"/>
  </g>
</svg>

<div class="abs art" style="left:205px;top:1055px;width:305px;height:255px" role="img" aria-label="Line illustration of a calculator, coins and a rising growth arrow"></div>
<div class="abs service" style="left:632px;top:1086px">
  <h3>FINANCIAL PLANNING</h3>
  <p>Lorem ipsum dolor sit amet, consectetur adipiscing elit, sed do eiusmod tempor incididunt ut labore et dolore magna aliqua. Ut enim ad minim veniam, quis nostrud exercitation ullamco laboris nisi ut aliquip ex ea commodo consequat.</p>
  <a class="btn-outline">LEARN MORE</a>
</div>

<div class="abs service" style="left:158px;top:1498px">
  <h3>ASSET MANAGEMENT</h3>
  <p>Lorem ipsum dolor sit amet, consectetur adipiscing elit, sed do eiusmod tempor incididunt ut labore et dolore magna aliqua. Ut enim ad minim veniam, quis nostrud exercitation ullamco laboris nisi ut aliquip ex ea commodo consequat.</p>
  <a class="btn-outline">LEARN MORE</a>
</div>
<div class="abs art" style="left:688px;top:1450px;width:282px;height:260px" role="img" aria-label="Line illustration of a money bag between two gears"></div>

<div class="abs art" style="left:205px;top:1845px;width:300px;height:235px" role="img" aria-label="Line illustration of a gear with a tick surrounded by four numbered steps"></div>
<div class="abs service" style="left:630px;top:1872px">
  <h3>PORTFOLIO OPTIMIZATION</h3>
  <p>Lorem ipsum dolor sit amet, consectetur adipiscing elit, sed do eiusmod tempor incididunt ut labore et dolore magna aliqua. Ut enim ad minim veniam, quis nostrud exercitation ullamco laboris nisi ut aliquip ex ea commodo consequat.</p>
  <a class="btn-outline">LEARN MORE</a>
</div>

<div class="abs service" style="left:133px;top:2260px">
  <h3>ALTERNATIVE INVESTMENTS</h3>
  <p>Lorem ipsum dolor sit amet, consectetur adipiscing elit, sed do eiusmod tempor incididunt ut labore et dolore magna aliqua. Ut enim ad minim veniam, quis nostrud exercitation ullamco laboris nisi ut aliquip ex ea commodo consequat.</p>
  <a class="btn-outline">LEARN MORE</a>
</div>
<div class="abs art" style="left:660px;top:2215px;width:300px;height:270px" role="img" aria-label="Line illustration of coin stacks, money bags and a connected line chart"></div>

<!-- ABOUT -->
<div class="abs" style="left:0;top:2580px;width:1200px;height:850px;background:linear-gradient(180deg,#e9edf1 0%,#f6f7f9 40%,#e8ecf0 100%)"></div>
<svg class="abs" style="left:0;top:2575px" width="1200" height="110" viewBox="0 0 1200 110">
  <path d="M0 0 H1200 V10 Q600 190 0 10 Z" fill="#fff"/>
</svg>
<div class="abs eyebrow" style="top:2762px">ABOUT US</div>
<div class="abs title" style="top:2780px">WHO WE ARE</div>
<p class="abs about-copy">Ravenholt Wealth is an investment advisory firm committed to serving as fiduciary to our clients. We always act in the best interests of our clients, including putting your interests ahead of our own.</p>
<div class="abs" style="left:0;top:3010px;width:1200px;height:420px;background:linear-gradient(180deg,rgba(236,240,244,0) 0%,#d7dde3 60%,#c9cfd6 100%)" role="img" aria-label="Paper sculptures of a bull and a bear facing each other in front of snowy mountains"></div>
<a class="abs btn-outline" style="left:542px;top:2950px;margin:0;padding:11px 32px">LEARN MORE</a>

<!-- WHY CHOOSE US -->
<div class="abs eyebrow" style="top:3487px">WHY WE ARE</div>
<div class="abs title" style="top:3505px">WHY CHOOSE US</div>
<svg class="abs" style="left:410px;top:3575px" width="380" height="380" viewBox="0 0 380 380">
  <circle cx="190" cy="190" r="176" fill="none" stroke="var(--blue-line)" stroke-width="2"/>
  <circle cx="59" cy="59" r="5" fill="#fff" stroke="var(--blue)" stroke-width="2"/>
  <circle cx="316" cy="54" r="5" fill="#fff" stroke="var(--blue)" stroke-width="2"/>
  <circle cx="30" cy="283" r="5" fill="#fff" stroke="var(--blue)" stroke-width="2"/>
  <circle cx="350" cy="272" r="5" fill="#fff" stroke="var(--blue)" stroke-width="2"/>
</svg>
<div class="abs" style="left:443px;top:3608px;width:310px;height:310px;border-radius:50%;background:linear-gradient(180deg,#2f86d6,#1a62b0 60%,#4c8fcf)" role="img" aria-label="Blue mountain lake scene inside a circular frame"></div>

<div class="abs feature" style="left:110px;top:3615px;width:200px;text-align:right"><h4>You Come First</h4><p>We always act in the best interests of our clients</p></div>
<div class="abs badge" style="left:325px;top:3598px"></div>
<div class="abs feature" style="left:872px;top:3600px;width:240px"><h4>Personalized Services</h4><p>We get to know you in order to service your unique needs</p></div>
<div class="abs badge" style="left:773px;top:3588px"></div>
<div class="abs feature" style="left:105px;top:3828px;width:195px;text-align:right"><h4>Transparent Fees</h4><p>You'll always know what you pay and how we get paid</p></div>
<div class="abs badge" style="left:325px;top:3818px"></div>
<div class="abs feature" style="left:892px;top:3818px;width:220px"><h4>We Give Back</h4><p>We support and better our local communities</p></div>
<div class="abs badge" style="left:783px;top:3808px"></div>

<!-- CONTACT -->
<div class="abs contact" style="left:0;top:4033px;width:1200px;height:600px;background:linear-gradient(180deg,#2a80cf,#1567b4 60%,#11579c)"></div>
<div class="abs contact" style="left:133px;top:4140px;width:340px">
  <h2>CONTACT US</h2>
  <p style="margin-top:12px;line-height:21px">Come to Ravenholt Wealth and find out how we can do better together.</p>
  <svg class="abs" style="left:0;top:135px" width="34" height="34" viewBox="0 0 34 34"><circle cx="17" cy="17" r="17" fill="#fff"/><path d="M17 8a6 6 0 0 0-6 6c0 5 6 11 6 11s6-6 6-11a6 6 0 0 0-6-6z" fill="var(--blue)"/><circle cx="17" cy="14" r="2.2" fill="#fff"/></svg>
  <span class="abs" style="left:44px;top:132px;width:290px;font-weight:700;line-height:28px;white-space:nowrap">2280 Alder Ridge Rd, Suite #140<br>Fairhollow, VA 20917</span>
  <svg class="abs" style="left:0;top:215px" width="34" height="34" viewBox="0 0 34 34"><circle cx="17" cy="17" r="17" fill="#fff"/><path d="M12 9l4 4-2 3c1 3 3 5 5 6l3-2 4 4-3 3c-8 0-15-7-15-15z" fill="var(--blue)"/></svg>
  <span class="abs" style="left:44px;top:222px;font-weight:700;white-space:nowrap">(555) 214-0937</span>
  <a class="abs" style="left:0;top:285px;border:2px solid #fff;color:#fff;font-family:Montserrat,sans-serif;font-weight:700;font-size:13px;padding:13px 34px;white-space:nowrap">CALL US NOW</a>
</div>

<div class="abs" style="left:528px;top:4123px;width:537px;height:381px;background:#fff;border-radius:90px 0 0 0">
  <div class="field" style="left:55px;top:50px"><label>First Name</label><div>John</div></div>
  <div class="field" style="left:290px;top:50px"><label>Last Name</label><div>Smith</div></div>
  <div class="field" style="left:55px;top:123px"><label>Email address</label><div>john@example.com</div></div>
  <div class="field" style="left:290px;top:123px"><label>Phone</label><div>+123 456 7890</div></div>
  <div class="field" style="left:55px;top:200px;width:453px;height:73px"><label>Message</label></div>
  <a class="abs" style="left:57px;top:297px;background:var(--blue);color:#fff;font-family:Montserrat,sans-serif;font-weight:700;font-size:12px;padding:13px 30px;white-space:nowrap">SEND MESSAGE</a>
</div>

<!-- FOOTER -->
<div class="abs footer" style="left:0;top:4560px;width:1200px;height:474px;background:var(--black)"></div>
<svg class="abs" style="left:0;top:4535px" width="1200" height="100" viewBox="0 0 1200 100">
  <path d="M0 0 Q600 120 1200 0 V100 H0 Z" fill="var(--black)"/>
  <path d="M150 45 Q600 120 1050 45" fill="none" stroke="var(--blue)" stroke-width="5"/>
</svg>
<div class="abs footer" style="left:120px;top:4730px;width:330px">
  <div class="head-font" style="font-size:22px;font-weight:500;letter-spacing:1px;white-space:nowrap">RAVENHOLT WEALTH</div>
  <p style="font-size:12.5px;line-height:16px;color:#cfd3d7;margin-top:28px">Lorem ipsum dolor sit amet, consectetur adipiscing elit, sed do eiusmod tempor incididunt ut labore et dolore</p>
</div>
<div class="abs footer rule" style="left:478px;top:4710px;height:160px"></div>
<div class="abs footer" style="left:502px;top:4712px"><h5>NAVIGATION</h5>
  <ul style="margin-top:12px"><li>Home</li><li>About Us</li><li>Services</li><li>FAQ</li><li>Contact Us</li></ul></div>
<div class="abs footer rule" style="left:688px;top:4710px;height:160px"></div>
<div class="abs footer" style="left:710px;top:4712px;width:220px"><h5>CONTACT US</h5>
  <svg class="abs" style="left:0;top:40px" width="26" height="26" viewBox="0 0 34 34"><circle cx="17" cy="17" r="17" fill="#fff"/><path d="M17 8a6 6 0 0 0-6 6c0 5 6 11 6 11s6-6 6-11a6 6 0 0 0-6-6z" fill="#000"/></svg>
  <p class="abs" style="left:36px;top:36px;width:200px;font-size:12.5px;line-height:20px;white-space:nowrap">2280 Alder Ridge Rd, Suite #140<br>Fairhollow, VA 20917</p>
  <svg class="abs" style="left:0;top:100px" width="26" height="26" viewBox="0 0 34 34"><circle cx="17" cy="17" r="17" fill="#fff"/><path d="M12 9l4 4-2 3c1 3 3 5 5 6l3-2 4 4-3 3c-8 0-15-7-15-15z" fill="#000"/></svg>
  <p class="abs" style="left:36px;top:103px;font-size:13px;white-space:nowrap">(555) 214-0937</p></div>
<div class="abs footer rule" style="left:935px;top:4710px;height:100px"></div>
<div class="abs footer" style="left:963px;top:4712px"><h5>FOLLOW US</h5>
  <div style="margin-top:10px;width:36px;height:36px;border-radius:50%;background:#fff" role="img" aria-label="Social profile link"></div></div>
<div class="abs" style="left:0;top:4970px;width:1200px;height:1px;background:#333"></div>
<p class="abs footer" style="left:0;top:4982px;width:1200px;text-align:center;font-size:12px;color:#cfd3d7">© 2022 <u>Ravenholt Wealth</u> All Rights Reserved</p>

</body>
</html>
```